Investment Memorandum Document

IM for Harbourline Lending Fund - is the document that needs work

Make sure it is all done in MS WORD so that i or lawyers can edit some words if required

the IM is NOT final but its 95% of the way there. Maybe a few more pages and wording changes - but that is something i can do i guess or you can easier adjust

Just to typeset and pretty it all up - a few sample finished products have been uploaded for reference.

QOR IM is the one i like - but feel free to show off your skills

put 1.2 to 1.8 all in contrasting row tables

Target Market(s)

Individual and Institutional investors with money

Industry/Entity Type

Investment Banking

Colors

Designer to choose colors to be used in the design.

Requirements
Must have
• clear professional layout and easy on the eye
• https://www.filecrate-example.net/sh/58k3p71zqx4mwtb/BBDrqLwZmUPxTvnQAHMDE42Kb?dl=0
• use the link above for high res images
Nice to have
• pictures and graphics
Should not have
• cartoons

```html
<!DOCTYPE html>
<html lang="en">
<head>
<meta charset="utf-8">
<title>Kestrel Commercial Income Fund – Information Memorandum</title>
<link rel="stylesheet" href="https://fonts.googleapis.com/css2?family=Arimo:ital,wght@0,400;0,700;1,400&display=swap">
<style>
  :root {
    --paper: #ffffff;
    --ink: #1a1a1a;
    --ink-soft: #444444;
    --gold-deep: #a9792a;
    --gold: #d9a520;
    --gold-bright: #f6c21c;
    --gold-pale: #fbeea8;
    --gold-mist: #fdf6d2;
    --highlight: #fff200;
    --shadow: rgba(0, 0, 0, 0.45);
  }
  * { box-sizing: border-box; margin: 0; padding: 0; }
  html, body { width: 1200px; height: 893px; overflow: hidden; background: #ffffff; }
  body { position: relative; font-family: "Arimo", Arial, sans-serif; color: var(--ink); }

  .page {
    position: absolute;
    background: var(--paper);
    overflow: hidden;
    box-shadow: 4px 5px 7px var(--shadow);
  }
  .cover { left: 58px; top: 82px; width: 499px; height: 705px; }
  .inner { top: 82px; width: 286px; height: 403px; padding: 34px 20px 0 24px; }
  .page-tax { left: 588px; }
  .page-notice { left: 890px; }

  .cover-art { position: absolute; inset: 0; }
  .corner-motif {
    position: absolute;
    background: radial-gradient(ellipse at 60% 40%, var(--gold) 0%, var(--gold-pale) 45%, rgba(253,246,210,0) 75%);
    opacity: 0.75;
  }
  .cover .corner-motif { left: 300px; top: 4px; width: 190px; height: 200px; }
  .inner .corner-motif { right: 0; top: 0; width: 110px; height: 46px; }

  .cover-title {
    position: absolute; left: 30px; right: 4px; top: 346px;
    text-align: center; font-size: 23.5px; line-height: 27px; font-weight: 400; color: #111;
  }
  .cover-parties { position: absolute; right: 18px; top: 546px; text-align: right; }
  .party-role { font-size: 15px; margin-bottom: 7px; }
  .party-name { font-size: 10.5px; margin-bottom: 22px; }

  .section-title { font-size: 6.5px; font-weight: 700; margin-bottom: 5px; }
  .section-title .num { display: inline-block; width: 14px; }
  .tax-body { padding-left: 14px; }
  .copy { font-size: 4.3px; line-height: 5.4px; color: var(--ink-soft); margin-bottom: 3px; }
  .placeholder { display: inline-block; margin: 6px 0 0 4px; font-size: 4.4px; font-weight: 700; background: var(--highlight); padding: 0 2px; }
  .notice-title { font-size: 6px; font-weight: 700; margin-bottom: 4px; }
  .clause-head { font-size: 4.3px; font-weight: 700; margin: 3px 0 1px; }
  .page-notice .copy { margin-bottom: 2.4px; line-height: 5.2px; }

  .page-footer {
    position: absolute; left: 0; right: 0; bottom: 0; height: 36px;
    display: flex; align-items: flex-end; justify-content: space-between;
    padding: 0 10px 8px 26px;
    background: linear-gradient(90deg, #ffffff 0%, #ffffff 70%, var(--gold-pale) 70%, var(--gold-pale) 100%);
  }
  .footer-label { font-size: 3.8px; font-style: italic; color: var(--ink-soft); }
  .footer-brand { display: flex; align-items: center; gap: 3px; font-size: 4px; font-weight: 700; color: var(--gold-deep); }
  .footer-brand .mark { width: 9px; height: 9px; background: var(--gold-deep); }
  .footer-page { font-size: 3.8px; font-style: italic; color: var(--ink-soft); }
</style>
</head>
<body>

  <section class="page cover">
    <svg class="cover-art" width="499" height="705" viewBox="0 0 499 705" role="img" aria-label="Gold diagonal cover band">
      <defs>
        <linearGradient id="goldBand" x1="1" y1="0" x2="0" y2="1">
          <stop offset="0" stop-color="#f8c91e"/>
          <stop offset="0.5" stop-color="#e2aa22"/>
          <stop offset="1" stop-color="#a9792a"/>
        </linearGradient>
        <linearGradient id="paleBand" x1="0" y1="0" x2="1" y2="1">
          <stop offset="0" stop-color="#fdf6d2"/>
          <stop offset="1" stop-color="#f8e68c"/>
        </linearGradient>
      </defs>
      <rect x="30" y="70" width="250" height="250" rx="34" fill="url(#paleBand)" transform="rotate(45 155 195)"/>
      <rect x="-70" y="250" width="640" height="330" rx="40" fill="url(#goldBand)" transform="rotate(-45 250 415)"/>
    </svg>
    <div class="corner-motif" role="img" aria-label="Gold tile pattern decoration"></div>

    <h1 class="cover-title">Kestrel Commercial Income Fund<br>Information Memorandum</h1>

    <div class="cover-parties">
      <p class="party-role">Investment Manager</p>
      <p class="party-name">Northgate Asset Management Pty Ltd</p>
      <p class="party-role">Trustee</p>
      <p class="party-name">Meridian Trust and Lending Corporation Pty Ltd</p>
    </div>
  </section>

  <section class="page inner page-tax">
    <div class="corner-motif" role="img" aria-label="Gold tile pattern decoration"></div>
    <h2 class="section-title"><span class="num">7.</span>Taxation information</h2>
    <div class="tax-body">
      <p class="copy">The Trustee has engaged Calder Rowe, an award-winning and leading mid-sized chartered accounting group, to provide a general outline of the Australian tax implications of purchasing Units pursuant to this IM as well as the holding and disposing of such Units, which is contained in the following letter.</p>
      <p class="copy">Taxation laws are both complex and subject to change and Investors should obtain their own advice taking account of their own circumstances.</p>
      <span class="placeholder">[ Tax advisor to provide]</span>
    </div>
    <footer class="page-footer">
      <span class="footer-label">Northgate AM Kestrel Commercial Income Fund – Information Memorandum</span>
      <span class="footer-brand"><span class="mark"></span>Northgate<span class="footer-page">&nbsp;Page 20 of 27</span></span>
    </footer>
  </section>

  <section class="page inner page-notice">
    <div class="corner-motif" role="img" aria-label="Gold tile pattern decoration"></div>
    <h2 class="notice-title">Notice</h2>
    <p class="copy">This information memorandum is dated XXX and is issued by Meridian Trust and Lending Corporation Pty Ltd ACN 000 000 000, holder of AFS licence number 000000 (Trustee), which is the trustee of the Kestrel Commercial Income Fund (Fund).</p>
    <p class="copy">The purpose of this IM is to provide information for prospective investors to decide whether they wish to invest in the Fund.</p>
    <p class="copy">The Trustee has appointed Northgate Asset Management Pty Ltd (Investment Manager) as the investment manager of the Fund under the Investment Management Agreement. The Investment Manager is an authorised representative of the Trustee.</p>
    <p class="copy">The Fund's trust deed (Trust Deed) provides for different Classes of Units. Different Classes of Units may have different rights and obligations. The performance of different Classes may also differ. Holders of Units will be treated fairly.</p>
    <h3 class="clause-head">NO DISCLOSURE REQUIRED</h3>
    <p class="copy">This IM is intended to provide potential investors with information only and does not constitute a product disclosure statement or other disclosure document required by the Corporations Act 2001 (Cth) (Act). This IM has not been lodged with ASIC or any other government body.</p>
    <p class="copy">The offer made under this IM is only available to persons who qualify as wholesale clients or sophisticated investors (collectively Qualified Investors). The Trustee will not issue Units to a person unless it is satisfied that the person is a Qualified Investor.</p>
    <h3 class="clause-head">RESTRICTIONS ON DISTRIBUTION</h3>
    <p class="copy">This IM does not constitute, and may not be used for the purposes of, an offer of Units or an invitation to apply for Units by any person in any jurisdiction in which such offer or invitation is not authorised, or to any person to whom it is unlawful to make such an offer.</p>
    <p class="copy">No action has been taken to register or qualify interests in the Fund, the invitation to participate in the Fund, or to otherwise permit any public offering of Fund interests in any jurisdiction other than Australia. It is the responsibility of prospective investors to satisfy themselves as to full compliance with the relevant laws of any jurisdiction.</p>
    <p class="copy">By receiving and viewing this IM, the recipient is warranting that they are legally entitled to do so and that the securities laws of their relevant jurisdiction do not prohibit them from acquiring interests in the Fund.</p>
    <p class="copy">In particular, this product has not been and will not be registered under the US Securities Act or the securities laws of any state of the United States and may not be offered, sold or transferred in the United States.</p>
    <p class="copy">With respect to Australian jurisdiction, this IM has been prepared on the basis that prospective Investors are wholesale clients or sophisticated investors, not retail clients within the meaning of the Act.</p>
    <p class="copy">Accordingly, this IM is not a product disclosure statement and does not contain all of the information that would be included in a product disclosure statement.</p>
    <p class="copy">The Trustee may in the future take actions to offer interests in the Fund in other jurisdictions.</p>
    <h3 class="clause-head">NO RESPONSIBILITY FOR CONTENTS OF DOCUMENT</h3>
    <p class="copy">To the maximum extent permitted by law, none of the Trustee, the Investment Manager, or any of their associates, related parties, directors, officers, employees or advisors makes any recommendation in relation to the Fund or makes any representation or warranty as to the accuracy, reliability or completeness of the information contained in this IM.</p>
    <p class="copy">This IM does not purport to contain all the information that a prospective Investor may require in evaluating a possible investment in the Fund.</p>
    <p class="copy">This IM must be read in conjunction with the Fund's Trust Deed which is available free of charge by contacting the Trustee on +61 3 9000 4172. To the extent there are any inconsistencies between the Trust Deed and this IM, the Trust Deed will prevail.</p>
    <h3 class="clause-head">NO DISTRIBUTION</h3>
    <p class="copy">Distribution of this IM to any person other than the persons receiving a copy of this IM from the Trustee or the Investment Manager is unauthorised. Any photocopying, disclosure or alteration of the contents of this IM, and any forwarding of this copy, is prohibited.</p>
    <h3 class="clause-head">NOT REGULATED BY APRA</h3>
    <footer class="page-footer">
      <span class="footer-label">Northgate AM Kestrel Commercial Income Fund – Information Memorandum</span>
      <span class="footer-brand"><span class="mark"></span>Northgate<span class="footer-page">&nbsp;Page 3 of 27</span></span>
    </footer>
  </section>

</body>
</html>
```